Eye surgeon needs a presentation folder and a business card for his practice manager. Logo alread...

I need a folder to put papers in when I am scheduling patients for surgery. The information is general, such as costs, consent forms etc. The folder is designed to give the patient these papers in a neat manner. The cover of the folder needs to use my brand and perhaps create some interest when it is sitting on their kitchen bench with visitors and family. I'll attach a typical template for a folder. It needs to be stylish, classic and professional, as I am about to operate on the person's eye. <br/>I would like my logo included. I'll also attach a photo which is on my website which might work to wrap around the folder. The website address is raybelford.com.au and you can see the way the image is used there on most of the pages as a banner. My profile photo could possibly used as well. Perhaps on the back, but if it looks strange then that is not necessary. The contact information need not be on the folder. Just Dr Ray Belford, Ophthalmic Surgeon. Finally, our brand slogan is. "The world's a beautiful place, see it clearly". This could also be on it. Again, this all needs to be professional looking. <br/>I've attached all our previous design jobs, 2 profile pictures, and the image that I think would work. Please also look at the website. <br/><br/>The second part of the project is to create a business card for my practice manager. Her name is Miriam Holtby<br/>It should include<br/>Miriam Holtby (BCom)<br/>Practice Manager for Dr Ray Belford<br/>Ophthalmic Surgeon <br/><br/>Then all the details which are on our current business card<br/><br/><br/><br/><br/>

Contact Information for Business Card

Just match the business cards I already have, but use the details above

Colors

Designer to choose colors to be used in the design.

```html
<!DOCTYPE html>
<html lang="en">
<head>
<meta charset="utf-8">
<title>Dr Ray Belford – Presentation Folder</title>
<link rel="stylesheet" href="https://fonts.googleapis.com/css2?family=Roboto:wght@400;700;900&display=swap">
<style>
  :root {
    --brand-blue: #0f6fb3;
    --brand-blue-deep: #0a5a98;
    --brand-blue-light: #2a9ad6;
    --ink-grey: #5a5f66;
    --paper: #ffffff;
    --band-grey: #eceef0;
    --stage: #e4e5e7;
    --photo-warm: #c9955a;
    --photo-top: #9a8a74;
    --photo-dark: #2a241d;
  }
  * { margin: 0; padding: 0; box-sizing: border-box; }
  html, body {
    width: 1200px;
    height: 847px;
    overflow: hidden;
    background: var(--stage);
    font-family: "Roboto", sans-serif;
  }
  .folder-spread {
    position: absolute;
    left: 140px;
    top: 98px;
    width: 920px;
    height: 650px;
    display: flex;
    box-shadow: 0 18px 40px rgba(0,0,0,0.18);
  }
  .folder-panel {
    width: 460px;
    height: 650px;
    display: block;
  }
  .brand-name { font-family: "Roboto", sans-serif; font-weight: 700; fill: var(--brand-blue); }
  .brand-role { font-family: "Roboto", sans-serif; font-weight: 700; fill: var(--ink-grey); }
  .brand-creds { font-family: "Roboto", sans-serif; font-weight: 400; fill: var(--ink-grey); }
  .slogan { font-family: "Roboto", sans-serif; font-weight: 900; fill: var(--paper); }
</style>
</head>
<body>
  <main class="folder-spread">

    <!-- Back cover -->
    <svg class="folder-panel back-cover" viewBox="0 0 460 650" xmlns="http://www.w3.org/2000/svg">
      <defs>
        <radialGradient id="backGlow" cx="0.45" cy="0.5" r="0.7">
          <stop offset="0" stop-color="var(--brand-blue-light)"/>
          <stop offset="1" stop-color="var(--brand-blue-deep)"/>
        </radialGradient>
        <linearGradient id="portraitTone" x1="0" y1="0" x2="1" y2="1">
          <stop offset="0" stop-color="#c9c6bd"/>
          <stop offset="0.5" stop-color="#b38a70"/>
          <stop offset="1" stop-color="#2b2d33"/>
        </linearGradient>
      </defs>
      <rect class="back-field" width="460" height="650" fill="url(#backGlow)"/>

      <g class="profile-photo">
        <rect x="148" y="372" width="180" height="180" fill="var(--paper)"/>
        <rect x="153" y="377" width="170" height="175" fill="url(#portraitTone)" role="img" aria-label="Profile photograph of Dr Ray Belford"/>
      </g>

      <path class="name-band" d="M0 560 Q230 520 460 440 L460 650 L0 650 Z" fill="var(--band-grey)"/>
      <path class="name-band-highlight" d="M0 566 Q230 526 460 446 L460 650 L0 650 Z" fill="var(--paper)" opacity="0.6"/>

      <g class="brand-lockup">
        <circle cx="92" cy="598" r="16" fill="var(--brand-blue)"/>
        <text class="brand-name" x="118" y="598" font-size="24">Dr Ray Belford</text>
        <text class="brand-role" x="119" y="613" font-size="9">Ophthalmic Surgeon</text>
        <text class="brand-creds" x="119" y="624" font-size="7">MBBS (Hons) MMed FRANZCO</text>
      </g>
    </svg>

    <!-- Front cover -->
    <svg class="folder-panel front-cover" viewBox="0 0 460 650" xmlns="http://www.w3.org/2000/svg">
      <defs>
        <linearGradient id="bannerTone" x1="0" y1="0" x2="0" y2="1">
          <stop offset="0" stop-color="var(--photo-top)"/>
          <stop offset="0.45" stop-color="var(--photo-warm)"/>
          <stop offset="1" stop-color="var(--photo-dark)"/>
        </linearGradient>
        <clipPath id="photoClip">
          <path d="M0 232 Q260 190 460 95 L460 650 L0 650 Z"/>
        </clipPath>
      </defs>

      <rect class="front-paper" width="460" height="650" fill="var(--paper)"/>

      <g class="brand-lockup">
        <circle cx="58" cy="70" r="18" fill="var(--brand-blue)"/>
        <text class="brand-name" x="86" y="72" font-size="27">Dr Ray Belford</text>
        <text class="brand-role" x="88" y="88" font-size="10">Ophthalmic Surgeon</text>
        <text class="brand-creds" x="88" y="99" font-size="7.5">MBBS (Hons) MMed FRANZCO</text>
      </g>

      <path class="swoosh" d="M0 200 Q250 165 460 70 L460 95 Q260 190 0 232 Z" fill="var(--brand-blue)"/>

      <rect class="banner-photo" width="460" height="650" clip-path="url(#photoClip)" fill="url(#bannerTone)" role="img" aria-label="Photograph of a sunset over the ocean"/>

      <g class="slogan-block" text-anchor="middle">
        <text class="slogan" x="245" y="485" font-size="22">The World's a Beautiful Place,</text>
        <text class="slogan" x="245" y="515" font-size="22">See it Clearly</text>
      </g>
    </svg>

  </main>
</body>
</html>
```